Sun Keel (www.sunkeel.com) web site development

Sun Keel is a new Fishing, Spearfishing Charter operator offering private charters in North Belize, Turneffe, Lighthouse Reef and the Blue Hole. The logo of the company has been designed by Pixelvane, some months ago. We have also developed a small brochure which can be the base for the website development (at least colors, fonts, etc.).
Pictures and Video should be an important asset of this website. We need to be able to update contents (video, photos), update prices and destinations, etc.

Target Market(s)

High hand, fishing and spearfishing enthusiasts.

Industry/Entity Type

Yacht charter

Coding

Coded - Design and coding required

Number of Pages Required

4 page

Colors
EB3D1F
EC4F4E
F09395
F8D3D4
FCEDEE

Requirements
Must have
• Optimized for phone and tablet navigation, must be easy to update with photos and video, connected to our Reefgram and Tidebook page,

```html
<!DOCTYPE html>
<html lang="en">
<head>
<meta charset="utf-8">
<title>Sun Keel — Private Fishing Charters</title>
<link rel="stylesheet" href="https://fonts.googleapis.com/css2?family=Roboto+Condensed:ital,wght@0,400;0,700;1,700&family=Arimo:wght@400;700&display=swap">
<style>
:root{
  --navy:#23465a;
  --red:#e4262f;
  --red-soft:#ec4f4e;
  --teal:#2c5b71;
  --teal-band:#4b7b92;
  --paper:#f4f2ed;
  --footer:#f6f3ee;
  --white:#ffffff;
  --ink:#3d4d57;
}
*{margin:0;padding:0;box-sizing:border-box}
html,body{width:1200px;height:1200px;overflow:hidden;background:var(--white)}
body{font-family:"Arimo",Arial,sans-serif;color:var(--ink);position:relative}
.page{position:absolute;left:390px;top:0;width:419px;height:1200px}
.abs{position:absolute}

/* hero */
.hero{left:0;top:0;width:419px;height:205px;background:linear-gradient(180deg,#a9c9f4 0%,#7fb0ea 40%,#2b6bb5 60%,#1c4f95 80%,#dfe9f3 100%)}
.brand{font-family:"Roboto Condensed",sans-serif;font-weight:700;color:var(--red);font-size:9px;display:flex;align-items:center;gap:3px}
.brand .dot{width:6px;height:6px;border-radius:50%;background:var(--red)}
.nav a{position:absolute;top:17px;font-family:"Roboto Condensed",sans-serif;font-weight:700;font-size:5px;letter-spacing:.3px;color:var(--navy);text-decoration:none;transform:translateX(-50%)}
.hero-rule{left:54px;top:30px;width:320px;height:1px;background:var(--red)}
.hero-title{left:165px;top:44px;font-family:"Roboto Condensed",sans-serif;font-style:italic;font-weight:700;font-size:25px;color:var(--navy);letter-spacing:.5px}
.hero-tag{left:165px;top:74px;font-family:"Roboto Condensed",sans-serif;font-size:7.5px;color:var(--navy)}
.hero-sub{left:165px;top:85px;font-size:5px;line-height:6.3px;color:var(--navy)}
.btn{display:flex;align-items:center;justify-content:center;background:var(--red);color:var(--white);font-family:"Roboto Condensed",sans-serif;font-weight:700;font-size:3.4px;letter-spacing:.3px;border-radius:3px}

/* trips */
.trips{left:0;top:205px;width:419px;height:356px;background:var(--paper)}
.head-box{border-top:1.3px solid var(--navy);border-bottom:1.3px solid var(--navy);display:flex}
.head-box .icon{border-right:1.3px solid var(--navy);display:flex;align-items:center;justify-content:center}
.head-title{font-family:"Roboto Condensed",sans-serif;font-weight:700;color:var(--red);letter-spacing:1px}
.trip-head{left:31px;top:256px;width:175px;height:27px}
.trip-head .icon{width:30px}
.trip-head .text{flex:1;text-align:center;padding-top:3px}
.trip-head .head-title{font-size:10px}
.trip-head .places{font-family:"Roboto Condensed",sans-serif;font-size:3.5px;color:var(--navy);font-weight:700;margin-top:1px}
.places i{display:inline-block;width:2px;height:2px;border-radius:50%;background:var(--red);margin:0 2px;vertical-align:middle}
.incl{font-size:6px;color:var(--navy);display:flex;align-items:center;gap:3px}
.incl svg{width:6px;height:6px}
.note{left:73px;top:341px;width:140px;font-size:4px;line-height:7px}
.footnote{left:73px;top:357px;font-size:2.6px}
.about-box{left:243px;top:236px;width:145px;height:146px;border:1.3px solid var(--navy);background:var(--white)}
.about-box p{position:absolute;left:14px;width:118px;font-size:3.9px;line-height:7.2px}
.about-box .btn{left:15px;top:111px;width:45px;height:12px;border-radius:2px}
.shot{background:linear-gradient(160deg,#5aa2d6,#1e5b8c)}
.social-tile{left:152px;top:407px;width:115px;height:114px;background:linear-gradient(180deg,#2d8fbf,#14506e 60%,#6b3a3a);display:flex;flex-direction:column;align-items:center;justify-content:center;color:var(--white)}
.social-tile .ring{width:13px;height:13px;border:1.3px solid var(--white);border-radius:50%;margin-bottom:17px}
.social-tile .label{font-family:"Roboto Condensed",sans-serif;font-weight:700;font-size:9px;text-align:center;line-height:14px}

/* adventure */
.adventure{left:0;top:561px;width:419px;height:279px;background:linear-gradient(135deg,#3a7a96,var(--teal) 45%,#24506a)}
.adv-head{left:61px;top:594px;width:297px;height:26px}
.adv-head.head-box{border-top-color:#e8eef2;border-bottom-color:#e8eef2}
.adv-head .icon{width:31px;border-right-color:#e8eef2}
.adv-head .text{padding-left:14px;display:flex;align-items:center;font-family:"Roboto Condensed",sans-serif;font-weight:700;font-size:9.5px;letter-spacing:1.2px;color:var(--white)}
.adv-head .text span{color:var(--red);margin-left:3px}
.adv-copy{left:97px;top:630px;width:222px;font-size:4.1px;line-height:7.1px;color:#e3ecf1}
.card{top:671px;width:114px;height:136px;background:var(--white)}
.card .band{height:14px;background:var(--teal-band);color:var(--white);font-size:4.5px;letter-spacing:.5px;display:flex;align-items:center;justify-content:center;font-family:"Roboto Condensed",sans-serif}
.card .price{margin-top:10px;text-align:center;font-family:"Roboto Condensed",sans-serif;font-weight:700;font-size:7.5px;color:var(--navy)}
.card .cap{text-align:center;font-size:2.8px;margin-top:1px}
.card .rule{width:36px;height:.8px;background:var(--red);margin:5px auto 5px}
.card p{padding:0 10px;font-size:3.9px;line-height:7.2px}
.card .book{position:absolute;left:10px;top:117px;font-family:"Roboto Condensed",sans-serif;font-weight:700;font-size:4.2px;color:var(--red);display:flex;align-items:center;gap:2px}

/* vessel */
.vessel-bg{left:0;top:840px;width:419px;height:237px;background:#faf9f6}
.vessel-head{left:64px;top:879px;width:297px;height:26px}
.vessel-head .icon{width:30px}
.vessel-head .text{flex:1;display:flex;align-items:center;justify-content:center}
.vessel-head .head-title{font-size:10px}
.vessel-photo{left:64px;top:925px;width:150px;height:87px;background:linear-gradient(180deg,#4f9be0 0%,#8fc3ef 45%,#3b86c7 60%,#1e5f9c 100%)}
.spec-box{left:201px;top:941px;width:160px;height:97px;border:1.3px solid var(--navy);background:var(--white)}
.spec-box h3{position:absolute;left:0;width:100%;top:17px;padding-left:20px;text-align:center;font-family:"Roboto Condensed",sans-serif;font-size:6px;color:var(--navy)}
.spec-box .desc{position:absolute;left:24px;top:26px;font-size:3.9px;line-height:7px}
.spec-box .rule{position:absolute;left:43px;top:44px;width:54px;height:.8px;background:var(--red)}
.spec-box dl{position:absolute;top:51px;font-size:3.6px;line-height:8.8px}
.spec-box dt{display:inline;font-weight:700;color:var(--navy)}
.spec-box dd{display:inline}

/* footer */
.footer{left:0;top:1077px;width:419px;height:123px;background:var(--footer)}
.f-rule{height:.8px;background:var(--red-soft)}
.addr{left:0;width:419px;top:1145px;text-align:center;font-size:3px;line-height:5px;font-style:normal}
.flinks a{position:absolute;top:1168px;transform:translateX(-50%);font-family:"Roboto Condensed",sans-serif;font-weight:700;font-size:3.4px;color:var(--navy);text-decoration:none}
</style>
</head>
<body>
<main class="page">

  <header class="abs hero" role="img" aria-label="Photo of a sport-fishing boat at sea with a marlin leaping from the waves"></header>
  <div class="abs brand" style="left:54px;top:17px"><span class="dot"></span>Sun Keel</div>
  <nav class="nav">
    <a style="left:253px" href="#">ABOUT US</a>
    <a style="left:308px" href="#">FISHING CHARTERS</a>
    <a style="left:360px" href="#">VESSEL</a>
  </nav>
  <div class="abs hero-rule"></div>
  <h1 class="abs hero-title">Sun Keel</h1>
  <div class="abs hero-tag">BIG FISH IS WHAT WE DO</div>
  <div class="abs hero-sub">Unforgettable Fishing, Spearfishing<br>&amp; Snorkeling Private Charters</div>
  <a class="abs btn" style="left:166px;top:107px;width:43px;height:12px">BOOK YOUR TRIP</a>

  <section class="abs trips" role="img" aria-label="Faded nautical chart of the Belize coast"></section>

  <div class="abs head-box trip-head">
    <div class="icon">
      <svg width="14" height="14" viewBox="0 0 14 14" fill="none" stroke="#23465a" stroke-width="1.2"><path d="M8 2v7a3 3 0 0 1-6 0"/><path d="M2 9l-1-1"/></svg>
    </div>
    <div class="text">
      <div class="head-title">ALL-INCLUSIVE TRIPS</div>
      <div class="places">NORTH BELIZE<i></i>TURNEFFE<i></i>LIGHTHOUSE REEF<i></i>BLUE HOLE</div>
    </div>
  </div>

  <div class="abs incl" style="left:76px;top:295px"><svg viewBox="0 0 10 10"><path d="M5 .5l1.3 3 3.2.3-2.4 2.1.7 3.2L5 7.4 2.2 9.1l.7-3.2L.5 3.8l3.2-.3z" fill="none" stroke="#23465a" stroke-width=".8"/></svg>Equipment</div>
  <div class="abs incl" style="left:76px;top:309px"><svg viewBox="0 0 10 10"><path d="M5 .5l1.3 3 3.2.3-2.4 2.1.7 3.2L5 7.4 2.2 9.1l.7-3.2L.5 3.8l3.2-.3z" fill="none" stroke="#23465a" stroke-width=".8"/></svg>Fuel</div>
  <div class="abs incl" style="left:76px;top:324px"><svg viewBox="0 0 10 10"><path d="M5 .5l1.3 3 3.2.3-2.4 2.1.7 3.2L5 7.4 2.2 9.1l.7-3.2L.5 3.8l3.2-.3z" fill="none" stroke="#23465a" stroke-width=".8"/></svg>Captain</div>
  <div class="abs incl" style="left:155px;top:295px"><svg viewBox="0 0 10 10"><path d="M5 .5l1.3 3 3.2.3-2.4 2.1.7 3.2L5 7.4 2.2 9.1l.7-3.2L.5 3.8l3.2-.3z" fill="none" stroke="#23465a" stroke-width=".8"/></svg>Guide</div>
  <div class="abs incl" style="left:155px;top:309px"><svg viewBox="0 0 10 10"><path d="M5 .5l1.3 3 3.2.3-2.4 2.1.7 3.2L5 7.4 2.2 9.1l.7-3.2L.5 3.8l3.2-.3z" fill="none" stroke="#23465a" stroke-width=".8"/></svg>Drinks*</div>
  <div class="abs incl" style="left:155px;top:324px"><svg viewBox="0 0 10 10"><path d="M5 .5l1.3 3 3.2.3-2.4 2.1.7 3.2L5 7.4 2.2 9.1l.7-3.2L.5 3.8l3.2-.3z" fill="none" stroke="#23465a" stroke-width=".8"/></svg>Lunch</div>
  <p class="abs note">Our trips also include your fresh caught fish cooked in the best grill restaurant in Caye Caulker (Drinks not included).</p>
  <p class="abs footnote">*only soft drinks for divers</p>

  <aside class="abs about-box">
    <p style="top:15px">Sun Keel offers fishing , spearfishing and snorkeling private charters in North Belize, Turneffe, Lighthouse Reef and the Blue Hole. No need to board crowded boats. Choose your privacy and let us pamper you with our exclusive service.</p>
    <p style="top:58px">Whether it is snorkeling for the family, tuna for the experienced angler, or deep sea spearfishing for the fight of a lifetime, you will surely be pleased. Not only do we offer a vast assortment of trips but our local guides will coach you through each fight to ensure you catch your desired trophy fish.</p>
    <a class="abs btn">BOOK YOUR TRIP</a>
  </aside>

  <div class="abs shot" style="left:31px;top:407px;width:54px;height:54px" role="img" aria-label="Snorkeler swimming over a reef"></div>
  <div class="abs shot" style="left:92px;top:407px;width:54px;height:54px;background:linear-gradient(160deg,#7eb1d8,#2f5f86)" role="img" aria-label="Angler holding a large jack"></div>
  <div class="abs shot" style="left:274px;top:407px;width:54px;height:54px;background:linear-gradient(160deg,#7aa6cf,#3b5e7c)" role="img" aria-label="Angler fighting a fish from the boat deck"></div>
  <div class="abs shot" style="left:334px;top:407px;width:54px;height:54px;background:linear-gradient(160deg,#8db8e0,#24507e)" role="img" aria-label="Marlin jumping beside the boat"></div>
  <div class="abs shot" style="left:31px;top:467px;width:54px;height:54px;background:linear-gradient(160deg,#3d9ad0,#135b8a)" role="img" aria-label="Spearfisher underwater with a catch"></div>
  <div class="abs shot" style="left:92px;top:467px;width:54px;height:54px;background:linear-gradient(160deg,#a6c3de,#4d6f8c)" role="img" aria-label="Group of anglers showing their catch"></div>
  <div class="abs shot" style="left:274px;top:467px;width:54px;height:54px;background:linear-gradient(160deg,#52a8d6,#2a6e9a)" role="img" aria-label="Snorkelers among a school of fish"></div>
  <div class="abs shot" style="left:334px;top:467px;width:54px;height:54px;background:linear-gradient(160deg,#7fb6e3,#3f6a4e)" role="img" aria-label="Two anglers holding a mahi-mahi"></div>
  <div class="abs social-tile" role="img" aria-label="Divers above a colourful coral reef">
    <span class="ring"></span>
    <span class="label">FOLLOW US ON<br>REEFGRAM</span>
  </div>

  <section class="abs adventure" role="img" aria-label="Underwater background of a dense school of fish"></section>
  <div class="abs head-box adv-head">
    <div class="icon">
      <svg width="13" height="15" viewBox="0 0 13 15" fill="none" stroke="#fff" stroke-width="1.1"><circle cx="6.5" cy="2" r="1.3"/><path d="M6.5 3.3V14M3.5 5.5h6M1 9.5a5.5 5 0 0 0 11 0"/></svg>
    </div>
    <div class="text">JUST BRING YOUR APPETITE FOR<span>ADVENTURE!</span></div>
  </div>
  <p class="abs adv-copy">We welcome both experienced fishermen/free divers and beginners. You can learn from our guides and even attend one of our introductory class to free dive and spearfishing from professional licensed instructors and expert scuba divers. You are welcome to take your gear with you, or leave us to provide you with all you need for an unforgettable experience. What you need to take with you is just your appetite for adventure.</p>

  <article class="abs card" style="left:31px">
    <div class="band">FISHING PRIVATE CHARTERS</div>
    <div class="price">FROM $1000</div>
    <div class="cap">(Maximum 6 guests 4 anglers)</div>
    <div class="rule"></div>
    <p>Our Fishing Charters are all Offshore Trips. Depending on your choice we can offer a variety of fishing options. For the experienced angler, test your skills by casting lures or if you're just a beginner bottom fishing baits is always a good way to go. We specialise in putting you on big fish and will do what it takes to make sure you get a chance to experience what drag screaming is all about.</p>
    <a class="book">BOOK TRIP <svg width="9" height="4" viewBox="0 0 9 4" fill="none" stroke="#e4262f" stroke-width=".7"><path d="M0 2h8M6 .5 8 2 6 3.5M1 .8l1 1.2-1 1.2"/></svg></a>
  </article>
  <article class="abs card" style="left:153px">
    <div class="band">SPEARFISHING PRIVATE CHARTERS</div>
    <div class="price">FROM $1400</div>
    <div class="cap">Maximum of 6 guests (4 divers)</div>
    <div class="rule"></div>
    <p>We welcome all experience levels and you will be accompanied by a safe diver in the water at all times to help you with anything you need! You are welcome to take along your equipment, however we provide the best equipment in the market. Our fishing grounds are all offshore so our Spearfishing Charters are a full day (minimum 8 hours).</p>
    <a class="book">BOOK TRIP <svg width="9" height="4" viewBox="0 0 9 4" fill="none" stroke="#e4262f" stroke-width=".7"><path d="M0 2h8M6 .5 8 2 6 3.5M1 .8l1 1.2-1 1.2"/></svg></a>
  </article>
  <article class="abs card" style="left:274px">
    <div class="band">SNORKELING PRIVATE CHARTERS</div>
    <div class="price">FROM $1200</div>
    <div class="cap">(Maximum 6 guests)</div>
    <div class="rule"></div>
    <p>We offer snorkeling trips to the Hole Chan Marine Reserve, Shark Ray Alley, Coral Gardens. All destinations inside the barrier reef and in calm waters. But we also offer snorkeling trips to the offshore Atolls: Turneffe North or South, Half Moon Caye National Park and the Blue Hole. Our Snorkeling Trips are full day (minimum 8 hours).</p>
    <a class="book">BOOK TRIP <svg width="9" height="4" viewBox="0 0 9 4" fill="none" stroke="#e4262f" stroke-width=".7"><path d="M0 2h8M6 .5 8 2 6 3.5M1 .8l1 1.2-1 1.2"/></svg></a>
  </article>

  <section class="abs vessel-bg" role="img" aria-label="Faded nautical chart of the cays"></section>
  <div class="abs head-box vessel-head">
    <div class="icon">
      <svg width="14" height="12" viewBox="0 0 14 12" fill="none" stroke="#23465a" stroke-width="1.2"><path d="M11 2a5 5 0 1 0 1 5"/><path d="M12 1v3h-3"/></svg>
    </div>
    <div class="text"><div class="head-title">OUR FISHING MACHINE</div></div>
  </div>
  <div class="abs vessel-photo" role="img" aria-label="White sport-fishing boat on turquoise water near the shore"></div>
  <div class="abs spec-box">
    <h3>CORVANE 290 OPEN</h3>
    <p class="desc">We outfit our boat with the latest electronics,<br>up to date safety gear and finest equipment.</p>
    <div class="rule"></div>
    <dl style="left:24px">
      <div><dt>LFT:</dt> <dd>31'10"</dd></div>
      <div><dt>BEAM:</dt> <dd>11'6"</dd></div>
      <div><dt>DRAFT:</dt> <dd>2'0"</dd></div>
      <div><dt>WEIGHT:</dt> <dd>10,000</dd></div>
    </dl>
    <dl style="left:72px">
      <div><dt>FUEL:</dt> <dd>302 GALS.</dd></div>
      <div><dt>WATER:</dt> <dd>55 GALS.</dd></div>
      <div><dt>ENGINES:</dt> <dd>2 X 350HP INBOARD</dd></div>
      <div><dt>CRUISE SPEED:</dt> <dd>20KN</dd></div>
    </dl>
  </div>

  <footer class="abs footer"></footer>
  <div class="abs f-rule" style="left:64px;top:1102px;width:297px"></div>
  <div class="abs brand" style="left:0;width:419px;top:1124px;justify-content:center;font-size:8px"><span class="dot"></span>Sun Keel</div>
  <address class="abs addr">Palm Reach Guesthouse<br>Playa Marea, Caye Caulker<br>Phone: 555-0142</address>
  <nav class="flinks">
    <a style="left:143px" href="#">ABOUT US</a>
    <a style="left:171px" href="#">VESSEL</a>
    <a style="left:207px" href="#">FISHING CHARTERS</a>
    <a style="left:246px" href="#">TIDEBOOK</a>
    <a style="left:278px" href="#">REEFGRAM</a>
  </nav>
  <div class="abs f-rule" style="left:67px;top:1183px;width:297px"></div>

</main>
</body>
</html>
```